Ledgerwise Systems Group business card design.

We are a software development company that develop Software for finance companies and related industries.

We need a 2 sided business card designed. We have a new logo already designed (see attached eps and ai) We are after a clean simple corporate look. One side with just our logo, and the second side with our details.

Mark Hollister
Managing Director

Suite 4 Level 9, 138 Kellaway Street Sydney NSW 2000

Direct: +61 2 9374 6021
Mobile: +61 4 2287 5196
Email: markh@lsg-example.net.au
Web: www.lsg-example.net.au

I have included 2 logo files an .ai and .eps. I noticed that the lines either side of the group looks a bit jaggered and needs to be made sharper.

I would like to introduce a little colour somewhere rather than having it all black and white. But not over the top, keeping with a simple clean corporate look. Perhaps a light blue on some of the text?

If you have other ideas would be pleased to review

Regards

Mark H.

```html
<!DOCTYPE html>
<html lang="en">
<head>
<meta charset="utf-8">
<title>Ledgerwise Systems Group — Business Card</title>
<link rel="stylesheet" href="https://fonts.googleapis.com/css2?family=Montserrat:wght@600&family=Questrial&display=swap">
<style>
  :root {
    --stage: #efefef;
    --card: #050505;
    --ink: #f4f4f4;
    --accent: #3aa6c9;
    --card-shadow: rgba(0, 0, 0, 0.22);
  }
  * { box-sizing: border-box; margin: 0; padding: 0; }
  html, body {
    width: 1200px;
    height: 720px;
    overflow: hidden;
    background: var(--stage);
  }
  .stage {
    position: relative;
    width: 1200px;
    height: 720px;
    display: flex;
    align-items: center;
    justify-content: center;
    gap: 60px;
  }
  .card {
    position: relative;
    width: 520px;
    height: 318px;
    background: var(--card);
    border-radius: 3px;
    box-shadow: 0 10px 24px var(--card-shadow);
    color: var(--ink);
    font-family: "Questrial", "Century Gothic", sans-serif;
  }

  /* Front: brand name */
  .card-front {
    display: flex;
    align-items: center;
    justify-content: center;
  }
  .brand {
    display: flex;
    align-items: center;
    gap: 14px;
  }
  .brand-mark {
    width: 30px;
    height: 30px;
    background: var(--ink);
  }
  .brand-name {
    font-family: "Montserrat", "Century Gothic", sans-serif;
    font-weight: 600;
    font-size: 21px;
    letter-spacing: 0.08em;
    text-transform: uppercase;
    color: var(--ink);
  }

  /* Back: contact details */
  .holder {
    position: absolute;
    left: 46px;
    top: 178px;
  }
  .holder-name {
    font-family: "Montserrat", "Century Gothic", sans-serif;
    font-weight: 600;
    font-size: 21px;
    letter-spacing: 0.02em;
    color: var(--ink);
  }
  .holder-role {
    margin-top: 2px;
    font-size: 14px;
    color: var(--accent);
  }
  .divider {
    position: absolute;
    left: 262px;
    top: 70px;
    width: 1px;
    height: 190px;
    background: linear-gradient(to bottom, transparent, var(--accent) 35%, var(--accent) 65%, transparent);
  }
  .details {
    position: absolute;
    left: 286px;
    top: 66px;
    font-size: 12.5px;
    line-height: 1.45;
  }
  .address { margin-bottom: 16px; }
  .contact-list {
    display: grid;
    grid-template-columns: 52px auto;
    row-gap: 1px;
  }
  .contact-label { color: var(--accent); }
  .contact-value { color: var(--ink); }
</style>
</head>
<body>
  <main class="stage">
    <section class="card card-front" aria-label="Business card front">
      <div class="brand">
        <span class="brand-mark" aria-hidden="true"></span>
        <span class="brand-name">Ledgerwise Systems Group</span>
      </div>
    </section>

    <section class="card card-back" aria-label="Business card back">
      <div class="holder">
        <p class="holder-name">Mark Hollister</p>
        <p class="holder-role">Managing Director</p>
      </div>
      <div class="divider" aria-hidden="true"></div>
      <div class="details">
        <p class="address">Suite 4 Level 9, 138<br>Kellaway Street Sydney<br>NSW 2000</p>
        <dl class="contact-list">
          <dt class="contact-label">Direct:</dt><dd class="contact-value">+61 2 9374 6021</dd>
          <dt class="contact-label">Mobile:</dt><dd class="contact-value">+61 4 2287 5196</dd>
          <dt class="contact-label">Email:</dt><dd class="contact-value">markh@lsg-example.net.au</dd>
          <dt class="contact-label">Web:</dt><dd class="contact-value">www.lsg-example.net.au</dd>
        </dl>
      </div>
    </section>
  </main>
</body>
</html>
```